Brent Halloway Design Contest (Just for Laughs)

Brent Halloway has lost some big sponsors recently: Quorvane, QL&N and Fizzlyne. He is also playing poor golf and may lose his #1 ranking soon. To remain the richest sportsman in the world (and to pay for his divorce) Brent needs some new sponsors and/or a new ad campaign for an existing sponsor. We would like you to come up with an endorsement, slogan and ad idea to help Brent reinvent himself and find a new sponsor and a new image!

Your task is to invent an advertisement (billboard or magazine) with Brent to promote a sponsor's product with a new slogan. The campaign you invent might be for one of his old sponsors like Olvo or QL&N or it might be for a new sponsor. Here are some ideas: dual sim card phones from QL&N; an adult website; helmets (that are golf club proof). You decide!

So come on designers, show us what you've got and have some fun!

Target Market(s)

Depends on the product Brent is endorsing.

Requirements
Nice to have
• A slogan, photogrpahy, a well known brand and humour.

```html
<!DOCTYPE html>
<html lang="en">
<head>
<meta charset="utf-8">
<title>I am Brent Halloway – Always Playing Through</title>
<link rel="stylesheet" href="https://fonts.googleapis.com/css2?family=Oswald:wght@500&family=Jost:wght@400;600&display=swap">
<style>
  :root {
    --ink-black: #000000;
    --accent-orange: #ec6a3c;
    --copy-white: #f2f2f2;
    --portrait-light: #9a9a9a;
    --portrait-mid: #3c3c3c;
  }
  * { margin: 0; padding: 0; box-sizing: border-box; }
  html, body {
    width: 1200px;
    height: 900px;
    overflow: hidden;
    background: var(--ink-black);
  }
  .ad {
    position: relative;
    width: 1200px;
    height: 900px;
    background: radial-gradient(ellipse at 30% 85%, #111111 0%, var(--ink-black) 60%);
    overflow: hidden;
  }
  .ad__portrait {
    position: absolute;
    left: 0;
    top: 0;
    width: 540px;
    height: 600px;
    background:
      radial-gradient(ellipse 52% 50% at 40% 36%, var(--portrait-light) 0%, var(--portrait-mid) 48%, rgba(0,0,0,0) 100%);
  }
  .ad__copy {
    position: absolute;
    left: 527px;
    top: 128px;
    width: 670px;
  }
  .ad__headline,
  .ad__slogan {
    font-family: "Oswald", "Arial Narrow", sans-serif;
    font-weight: 500;
    color: var(--accent-orange);
    font-size: 33px;
    line-height: 44px;
    letter-spacing: 0.2px;
  }
  .ad__lines {
    list-style: none;
    margin-top: 10px;
  }
  .ad__lines li {
    font-family: "Jost", "Futura", sans-serif;
    font-weight: 400;
    color: var(--copy-white);
    font-size: 21px;
    line-height: 47px;
    letter-spacing: 1.9px;
    white-space: nowrap;
  }
  .ad__slogan {
    margin-top: 4px;
  }
  .ad__brand {
    position: absolute;
    right: 78px;
    bottom: 58px;
    font-family: "Jost", "Futura", sans-serif;
    font-weight: 600;
    font-size: 56px;
    line-height: 1;
    color: var(--copy-white);
    letter-spacing: 1px;
  }
</style>
</head>
<body>
  <main class="ad">
    <div class="ad__portrait" role="img" aria-label="Black-and-white close-up portrait of Brent Halloway staring into the camera, fading into the black background"></div>

    <section class="ad__copy">
      <h1 class="ad__headline">I am Brent Halloway</h1>
      <ul class="ad__lines">
        <li>I travel the world, so lock up your daughters.</li>
        <li>I have a VIP pass to the Velvetine Mansion.</li>
        <li>I don’t have a little black book, I have a little black bible.</li>
        <li>I know how to re-arrange the back seats of my SUV quickly.</li>
        <li>I can say ‘what room are you in?” In 18 different languages.</li>
        <li>I understand what you mean when you say get in the hole.</li>
        <li>I don’t discriminate, I’ll sleep with any race of woman.</li>
        <li>I tip great, (if you know what I mean..wink, wink)</li>
        <li>I love to play in foursomes.</li>
        <li>I can play more than 18 holes in one day.</li>
        <li>I will be in your neighbourhood...call me.</li>
      </ul>
      <p class="ad__slogan">Always Playing Through.</p>
    </section>

    <div class="ad__brand">Olvo</div>
  </main>
</body>
</html>
```